Tradeshwo display 8x10 high resolution backdrop

I created a backdrop I wanted to use via Chat GPT but the image isn't high quality enough for print so I want someone to recreate it as close as possible to my creation. See attached, TY!

```html
<!DOCTYPE html>
<html lang="en">
<head>
<meta charset="utf-8">
<title>Ridgeway Flow Systems – Trade Show Backdrop</title>
<link rel="stylesheet" href="https://fonts.googleapis.com/css2?family=Barlow+Condensed:wght@600;700&family=Barlow+Semi+Condensed:wght@500;600;700;800&family=Barlow:wght@400;500;600&display=swap">
<style>
  :root{
    --navy:#0b1a3a;
    --navy-deep:#06122b;
    --ink:#0d0f14;
    --blue:#1747b8;
    --blue-bright:#2a6bf0;
    --blue-dark:#0f2f86;
    --line:#1e46a8;
    --grey-text:#2a2d33;
    --divider:#d6dbe4;
    --white:#ffffff;
  }
  *{box-sizing:border-box;margin:0;padding:0}
  html,body{width:1200px;height:800px;overflow:hidden;background:#fff}
  .backdrop{position:relative;width:1200px;height:800px;overflow:hidden;
    background:linear-gradient(180deg,#ffffff 0%,#f4f6fa 60%,#eef1f6 100%);
    font-family:"Barlow Semi Condensed",sans-serif;color:var(--ink)}
  .abs{position:absolute}

  /* brand */
  .brand{left:48px;top:72px;display:flex;align-items:center;gap:14px}
  .brand-dot{width:34px;height:34px;border-radius:50%;background:var(--blue)}
  .brand-name{font-weight:700;font-size:34px;line-height:1.0;color:var(--navy);width:220px}

  /* value icons */
  .values{left:378px;top:76px;display:flex;height:106px}
  .value{display:flex;flex-direction:column;align-items:center;justify-content:flex-start;
    border-left:1px solid #9aa4b5;text-align:center;font-weight:600;font-size:14px;line-height:18px;color:var(--ink)}
  .value svg{width:46px;height:46px;margin:4px 0 16px}
  .value:nth-child(1){width:93px}.value:nth-child(2){width:94px}
  .value:nth-child(3){width:87px}.value:nth-child(4){width:90px}

  /* photo */
  .photo{left:760px;top:0;width:440px;height:300px}

  /* headline */
  .headline{left:48px;top:214px}
  .headline .line1{font-weight:800;font-size:67px;line-height:62px;color:var(--ink);letter-spacing:.5px}
  .headline .line2{font-weight:800;font-size:79px;line-height:78px;letter-spacing:.5px;
    background:linear-gradient(180deg,#2b63e6 0%,#0f2f86 100%);-webkit-background-clip:text;background-clip:text;color:transparent}
  .tagline{left:50px;top:359px;width:730px;display:flex;align-items:center;gap:18px;
    font-family:"Barlow",sans-serif;font-size:15px;letter-spacing:3.5px;color:var(--ink)}
  .tagline::before,.tagline::after{content:"";flex:1;height:2px;background:var(--line)}
  .banner{left:0;top:391px;width:780px;height:42px;border-radius:0 10px 10px 0;
    background:linear-gradient(90deg,#0d2b78 0%,#1c4fc4 60%,#133a9c 100%);
    color:#fff;font-weight:600;font-size:18px;letter-spacing:4.3px;display:flex;align-items:center;padding-left:55px}

  /* feature panels */
  .features{left:895px;top:285px;width:305px}
  .feature{position:relative;display:flex;align-items:center;background:var(--navy-deep);
    clip-path:polygon(34px 0,100% 0,100% 100%,34px 100%,0 50%);margin-bottom:3px}
  .feature .icon{width:62px;height:62px;margin-left:32px;flex:none}
  .feature .text{margin-left:16px;padding-left:12px;border-left:1px solid #c8d2e6;
    color:#fff;font-weight:500;font-size:16px;line-height:19.5px;letter-spacing:.6px}
  .f1{height:92px}.f2{height:86px}.f3{height:86px}.f4{height:104px}

  /* products */
  .products{left:0;top:468px;width:894px;display:flex}
  .product{text-align:center;border-right:1px solid var(--divider);padding-top:6px;height:228px;flex:none}
  .product:last-child{border-right:none}
  .product .shot{height:118px;margin:0 auto 16px;border-radius:10px}
  .product h3{font-family:"Barlow Condensed",sans-serif;font-weight:700;font-size:16px;color:var(--blue);margin-bottom:6px;white-space:nowrap}
  .product p{font-family:"Barlow",sans-serif;font-size:10.2px;line-height:17.5px;color:var(--grey-text);padding:0 4px}
  .p1{width:170px}.p2{width:158px}.p3{width:162px}.p4{width:137px}.p5{width:137px}.p6{width:130px}
  .shot-blue{background:radial-gradient(circle at 50% 50%,#2d56b8 0%,#16307a 55%,transparent 72%)}
  .shot-grey{background:radial-gradient(circle at 50% 50%,#8e9298 0%,#55595f 55%,transparent 72%)}
  .shot-vfd{background:linear-gradient(180deg,#3c4047,#1b1e22)}

  /* footer */
  .footer{left:0;top:730px;width:1200px;height:70px;
    background:linear-gradient(90deg,#081634 0%,#0c2357 50%,#0a1c45 100%);color:#fff}
  .pin{left:28px;top:14px;width:42px;height:42px}
  .serving{left:80px;top:16px}
  .serving h4{font-family:"Barlow",sans-serif;font-weight:600;font-size:19px;line-height:20px}
  .serving p{font-family:"Barlow",sans-serif;font-size:13.5px;margin-top:3px;color:#e6ebf5}
  .vrule{top:16px;width:2px;height:38px;background:#fff}
  .web{left:485px;top:22px;display:flex;align-items:center;gap:8px;font-family:"Barlow",sans-serif;font-size:18px}
  .partner{left:840px;top:12px;font-family:"Barlow",sans-serif}
  .partner .small{font-size:16px;line-height:20px}
  .partner .big{font-weight:600;font-size:22px;line-height:26px;color:var(--blue-bright)}
</style>
</head>
<body>
<div class="backdrop">

  <div class="abs brand">
    <div class="brand-dot"></div>
    <div class="brand-name">Ridgeway Flow Systems</div>
  </div>

  <div class="abs values">
    <div class="value">
      <svg viewBox="0 0 48 48" fill="none" stroke="#1747b8" stroke-width="2.2" stroke-linejoin="round"><circle cx="24" cy="18" r="13"/><circle cx="24" cy="18" r="8"/><path d="M19 18l4 4 6-7"/><path d="M16 29l-5 13 7-3 4 5 2-10M32 29l5 13-7-3-4 5-2-10"/></svg>
      QUALITY<br>BRANDS
    </div>
    <div class="value">
      <svg viewBox="0 0 48 48" fill="none" stroke="#1747b8" stroke-width="2.2" stroke-linejoin="round"><path d="M21 4h6l1 6 5 2 5-4 4 4-4 5 2 5 6 1v6l-6 1-2 5 4 5-4 4-5-4-5 2-1 6h-6l-1-6-5-2-5 4-4-4 4-5-2-5-6-1v-6l6-1 2-5-4-5 4-4 5 4 5-2z"/><circle cx="24" cy="24" r="7"/></svg>
      ENGINEERED<br>SOLUTIONS
    </div>
    <div class="value">
      <svg viewBox="0 0 48 48" fill="none" stroke="#1747b8" stroke-width="2.2" stroke-linecap="round"><path d="M10 26v-4a14 14 0 0128 0v4"/><rect x="7" y="24" width="7" height="12" rx="3"/><rect x="34" y="24" width="7" height="12" rx="3"/><path d="M37 36c0 5-5 7-10 7"/><circle cx="25" cy="43" r="2"/></svg>
      EXPERT<br>SUPPORT
    </div>
    <div class="value">
      <svg viewBox="0 0 48 48" fill="none" stroke="#1747b8" stroke-width="2.2" stroke-linejoin="round" stroke-linecap="round"><path d="M3 16l8-4 8 4M45 16l-8-4-9 4-8 6 3 3 7-4 9 9"/><path d="M11 14l-6 14 5 5M37 14l6 14-6 5"/><path d="M12 31l3 3M16 28l5 5M20 25l5 5M27 34l3 3"/></svg>
      TURNKEY<br>DELIVERY
    </div>
  </div>

  <svg class="abs photo" viewBox="0 0 440 300" role="img" aria-label="Photo of a water treatment plant with circular clarifier tanks at sunset under a blue sky">
    <defs>
      <linearGradient id="sky" x1="0" y1="0" x2="0" y2="1">
        <stop offset="0" stop-color="#2d5fa8"/><stop offset=".35" stop-color="#8fb0d6"/>
        <stop offset=".48" stop-color="#f0c27a"/><stop offset=".56" stop-color="#2b3a4a"/>
        <stop offset=".75" stop-color="#4e6a8c"/><stop offset="1" stop-color="#1d2c46"/>
      </linearGradient>
    </defs>
    <path d="M10 0H440V300H200C150 250 60 120 10 0Z" fill="url(#sky)"/>
    <path d="M0 0C50 120 140 250 195 300H182C128 255 40 130 -6 0Z" fill="#1a4fc8"/>
  </svg>

  <div class="abs headline">
    <div class="line1">SOLUTIONS THAT</div>
    <div class="line2">KEEP WATER MOVING</div>
  </div>
  <div class="abs tagline">EXPERTISE. RELIABILITY. RESULTS.</div>
  <div class="abs banner">COMPLETE SOLUTIONS FOR THE WATER &amp; WASTEWATER INDUSTRY</div>

  <div class="abs features">
    <div class="feature f1">
      <svg class="icon" viewBox="0 0 62 62" fill="none" stroke="#2a6bf0" stroke-width="2.4"><circle cx="31" cy="31" r="28"/><path d="M31 13c-7 10-11 16-11 22a11 11 0 0022 0c0-6-4-12-11-22z"/><path d="M26 36a5 5 0 005 5"/></svg>
      <div class="text">WATER &amp;<br>WASTEWATER<br>EXPERTISE</div>
    </div>
    <div class="feature f2">
      <svg class="icon" viewBox="0 0 62 62" fill="none" stroke="#2a6bf0" stroke-width="2.4" stroke-linejoin="round"><path d="M31 4l22 8v16c0 15-10 25-22 30C19 53 9 43 9 28V12z"/><path d="M31 11l16 6v11c0 11-7 18-16 22-9-4-16-11-16-22V17z" fill="#2a6bf0"/><path d="M23 31l6 6 11-12" stroke="#06122b" stroke-width="3.5"/></svg>
      <div class="text">TRUSTED<br>PRODUCTS</div>
    </div>
    <div class="feature f3">
      <svg class="icon" viewBox="0 0 62 62" fill="none" stroke="#2a6bf0" stroke-width="3" stroke-linecap="round"><path d="M12 32v-6a19 19 0 0138 0v6"/><rect x="8" y="28" width="9" height="16" rx="4" fill="#2a6bf0"/><rect x="45" y="28" width="9" height="16" rx="4" fill="#2a6bf0"/><path d="M49 44c0 8-8 11-16 11"/><circle cx="31" cy="55" r="3" fill="#2a6bf0"/></svg>
      <div class="text">LOCAL SUPPORT<br>YOU CAN COUNT ON</div>
    </div>
    <div class="feature f4">
      <svg class="icon" viewBox="0 0 62 62" fill="none" stroke="#2a6bf0" stroke-width="2.4"><circle cx="31" cy="31" r="28"/><rect x="18" y="36" width="6" height="10" fill="#2a6bf0"/><rect x="27" y="30" width="6" height="16" fill="#2a6bf0"/><rect x="36" y="24" width="6" height="22" fill="#2a6bf0"/><path d="M17 30l12-10 6 5 10-9M40 16h5v5" stroke-linecap="round" stroke-linejoin="round"/></svg>
      <div class="text">BUILT FOR<br>PERFORMANCE.<br>FOCUSED ON<br>YOUR SUCCESS.</div>
    </div>
  </div>

  <div class="abs products">
    <div class="product p1">
      <div class="shot shot-blue" style="width:140px" role="img" aria-label="Product photo of a blue split-case centrifugal pump"></div>
      <h3>PUMPS</h3>
      <p>Industry leading pumps<br>built for performance,<br>efficiency &amp; reliability.</p>
    </div>
    <div class="product p2">
      <div class="shot shot-blue" style="width:130px" role="img" aria-label="Product photo of a blue industrial electric motor"></div>
      <h3>MOTORS</h3>
      <p>High efficiency motors<br>engineered for durability<br>and long life.</p>
    </div>
    <div class="product p3">
      <div class="shot shot-grey" style="width:130px" role="img" aria-label="Product photo of a grey positive displacement blower"></div>
      <h3>BLOWERS</h3>
      <p>Aeris PD positive displacement<br>blowers for reliable, energy<br>efficient performance.</p>
    </div>
    <div class="product p4">
      <div class="shot shot-vfd" style="width:56px;border-radius:3px" role="img" aria-label="Product photo of a variable frequency drive unit with keypad"></div>
      <h3>VFD &amp; CONTROLS</h3>
      <p>Precision control and<br>energy savings through<br>advanced VFD solutions.</p>
    </div>
    <div class="product p5">
      <div class="shot shot-blue" style="width:100px" role="img" aria-label="Product photo of an actuated blue flanged valve"></div>
      <h3>AUTOMATION &amp; VALVES</h3>
      <p>Smart automation and<br>reliable valves for optimized<br>system performance.</p>
    </div>
    <div class="product p6">
      <svg class="shot" style="width:100px;display:block" viewBox="0 0 100 118" fill="#1747b8">
        <path d="M44 14h12l2 7 6 3 6-4 8 8-4 6 3 6 7 2v12l-7 2-3 6 4 6-8 8-6-4-6 3-2 7H44l-2-7-6-3-6 4-8-8 4-6-3-6-7-2V42l7-2 3-6-4-6 8-8 6 4 6-3z"/>
        <circle cx="50" cy="48" r="16" fill="#fff"/>
        <path d="M50 37c-5 7-7 10-7 13a7 7 0 0014 0c0-3-2-6-7-13z"/>
        <path d="M18 96l16-12h20c4 0 4 6 0 6H44l2 2 20-10c5-3 9 3 4 6L46 104H18z"/>
      </svg>
      <h3>TURNKEY SOLUTIONS</h3>
      <p>Complete systems<br>designed, integrated<br>and supported by RFS.</p>
    </div>
  </div>

  <div class="abs footer">
    <svg class="abs pin" viewBox="0 0 42 42"><circle cx="21" cy="21" r="20" fill="#fff"/><circle cx="21" cy="21" r="17" fill="#1a4fc8"/><path d="M21 9a8 8 0 00-8 8c0 6 8 15 8 15s8-9 8-15a8 8 0 00-8-8z" fill="#fff"/><circle cx="21" cy="17" r="3" fill="#1a4fc8"/></svg>
    <div class="abs serving">
      <h4>SERVICING</h4>
      <p>Virginia &nbsp;|&nbsp; North Carolina &nbsp;|&nbsp; Maryland &nbsp;|&nbsp; Delaware</p>
    </div>
    <div class="abs vrule" style="left:436px"></div>
    <div class="abs web">
      <svg width="22" height="22" viewBox="0 0 22 22" fill="none" stroke="#fff" stroke-width="1.6"><circle cx="11" cy="11" r="9.5"/><ellipse cx="11" cy="11" rx="4" ry="9.5"/><path d="M1.5 11h19M3 6h16M3 16h16"/></svg>
      www.ridgewayflow-example.com
    </div>
    <div class="abs vrule" style="left:780px"></div>
    <div class="abs partner">
      <div class="small">Your Partner For</div>
      <div class="big">A BETTER FLOW FORWARD</div>
    </div>
  </div>

</div>
</body>
</html>
```